Trying to make a small (4.25" x 5.50") re-elect sticker for a congressman in california. The congressmans name is Corwin Haltby and we would like to change his last name to "Haltbovich". Basically we believe his relationship to Pimsworth/Lavrik should be reflected in this poster with russia undertones.

The idea behind this project is to reflect Corwin Haltby as a political puppet of Gerald Pimsworth who is also a puppet of Russian president Lavrik.
We do not support Corwin Haltby as our elected official and believe him to be a traitor to our district and a traitor to our country.
Trying to make a small (4.25" x 5.50") re-elect sticker for a congressman in California. The congressman's name is Corwin Haltby and we would like to change his last name to "Haltbovich". Basically we believe his relationship to Pimsworth/Lavrik should be reflected in this poster with Russia undertones.

Trying to make a small (4.25" x 5.50") re-elect sticker for a congressman in California. The congressman's name is Corwin Haltby and we would like to change his last name to "Haltbovich". Basically we believe his relationship to Pimsworth/Lavrik should be reflected in this poster with Russian undertones.

I have never done this type of project before so any advise would be helpful,any questions just email me thanks.
Oliver

Oliver

Target Market(s)

For political grass roots campaign.

Industry/Entity Type

Political

Colors

Designer to choose colors to be used in the design.

Requirements
Must have
• Picture of Corwin Haltby. Re-elect (переизбрание). Change last name to Haltbovich
Nice to have
• Maybe the hammer and sickle logo someplace but not too obvious
Should not have
• Nothing obscene or offensiveпереизбрание

```html
<!DOCTYPE html>
<html lang="en">
<head>
<meta charset="utf-8">
<title>Corwin Haltbovich — Re-elect Sticker</title>
<link rel="stylesheet" href="https://fonts.googleapis.com/css2?family=Anton&family=Arimo:wght@700&family=PT+Sans&display=swap">
<style>
  :root {
    --red-bright: #e0191b;
    --red-mid: #c0201c;
    --red-deep: #8e1410;
    --maroon: #8a0000;
    --maroon-shadow: #5a0000;
    --copper: #b4532e;
    --white: #ffffff;
    --pink: #f4b9bd;
  }
  html, body {
    margin: 0;
    padding: 0;
    overflow: hidden;
    background: #ffffff;
  }
  .sticker {
    position: relative;
    width: 1200px;
    height: 927px;
    overflow: hidden;
    background: linear-gradient(125deg, var(--red-mid) 0%, var(--red-bright) 40%, var(--red-deep) 100%);
  }
  .backdrop-art {
    position: absolute;
    left: 380px;
    top: 0;
    width: 820px;
    height: 660px;
    background:
      radial-gradient(ellipse at 45% 55%, rgba(210,110,60,0.75) 0%, rgba(170,60,35,0.55) 35%, rgba(150,30,25,0) 70%),
      linear-gradient(160deg, #c56b3f 0%, #a7352a 45%, #9b1f1c 100%);
    opacity: 0.9;
  }
  .bands {
    position: absolute;
    inset: 0;
  }
  .portrait {
    position: absolute;
    left: 97px;
    top: 160px;
    width: 430px;
    height: 800px;
    border-radius: 46% 46% 6% 6% / 32% 32% 4% 4%;
    background: linear-gradient(180deg, #3a2a22 0%, #3a2a22 14%, #d8a58a 22%, #cf9a80 55%, #b7c7d8 70%, #dfe4ea 85%, #c9ccd1 100%);
    box-shadow: 0 0 30px 14px rgba(255,255,255,0.85);
  }
  .name {
    position: absolute;
    left: 598px;
    margin: 0;
    font-family: "Anton", "Impact", sans-serif;
    font-weight: 400;
    line-height: 1;
    background: linear-gradient(120deg, var(--white) 0%, var(--white) 45%, var(--pink) 60%, var(--white) 75%, var(--pink) 100%);
    -webkit-background-clip: text;
    background-clip: text;
    color: transparent;
  }
  .name-first {
    top: 82px;
    font-size: 168px;
    letter-spacing: -2px;
  }
  .name-last {
    top: 252px;
    font-size: 140px;
    letter-spacing: -3px;
  }
  .tagline-ru {
    position: absolute;
    left: 604px;
    top: 416px;
    margin: 0;
    font-family: "PT Sans", "Arial", sans-serif;
    font-size: 74px;
    color: var(--white);
    line-height: 1;
    letter-spacing: 1px;
  }
  .corner-white {
    position: absolute;
    inset: 0;
  }
  .reelect-badge {
    position: absolute;
    left: 603px;
    top: 634px;
    width: 544px;
    height: 186px;
    background: var(--maroon);
    display: flex;
    align-items: center;
    justify-content: center;
    border: 2px solid rgba(255,255,255,0.35);
    box-sizing: border-box;
  }
  .reelect-text {
    font-family: "Arimo", "Arial", sans-serif;
    font-weight: 700;
    font-size: 100px;
    color: var(--white);
    letter-spacing: -1px;
  }
  .badge-fold {
    position: absolute;
    inset: 0;
  }
</style>
</head>
<body>
  <main class="sticker">
    <div class="backdrop-art" role="img" aria-label="Blurred red and copper background artwork with Russian-themed emblem"></div>

    <svg class="bands" width="1200" height="927" viewBox="0 0 1200 927" aria-hidden="true">
      <polygon points="0,0 300,0 0,420" fill="#c2231f" opacity="0.6"/>
      <polygon points="0,560 160,330 160,640 0,900" fill="#d9211f" opacity="0.55"/>
      <polygon points="520,927 760,560 900,560 680,927" fill="#e02321" opacity="0.45"/>
    </svg>

    <div class="portrait" role="img" aria-label="Portrait photo of Corwin Haltby in a light blue shirt and striped tie"></div>

    <h1 class="name name-first">Corwin</h1>
    <h1 class="name name-last">Haltbovich</h1>
    <p class="tagline-ru">переизбрание</p>

    <svg class="corner-white" width="1200" height="927" viewBox="0 0 1200 927" aria-hidden="true">
      <polygon points="1200,489 1200,927 724,927" fill="#ffffff"/>
    </svg>

    <svg class="badge-fold" width="1200" height="927" viewBox="0 0 1200 927" aria-hidden="true">
      <polygon points="1008,820 1147,820 1147,836 1008,865" fill="#5a0000"/>
    </svg>

    <div class="reelect-badge">
      <span class="reelect-text">Re-elect</span>
    </div>
  </main>
</body>
</html>
```